Informative 1-Pager website that informs users about the threat of ransomware

See current page: https://www.quellbrook-shield.com/

Coded - Design and coding required

```html
<!DOCTYPE html>
<html lang="en">
<head>
<meta charset="utf-8">
<title>Avoid Ransomware – Quellbrook Shield</title>
<link href="https://fonts.googleapis.com/css2?family=Poppins:wght@300;400;500;600&display=swap" rel="stylesheet">
<style>
:root{
  --navy:#0f2a48;
  --navy-deep:#0c1f38;
  --yellow:#fcc12d;
  --ink:#1d3654;
  --body:#6b7380;
  --light:#f7f7f7;
  --white:#ffffff;
}
*{margin:0;padding:0;box-sizing:border-box}
html,body{width:1200px;height:3688px;overflow:hidden}
body{font-family:"Poppins",sans-serif;color:var(--body);background:var(--white);position:relative}
.abs{position:absolute}

/* hero */
.hero{position:absolute;left:0;top:0;width:1200px;height:643px;background:linear-gradient(120deg,#0d1b2c 0%,#22344a 35%,#3a5470 50%,#1c2d42 70%,#0c1828 100%)}
.hero-photo{position:absolute;inset:0;background:radial-gradient(ellipse 260px 340px at 450px 330px,rgba(120,160,200,.35),transparent 70%)}
.topbar{position:absolute;left:0;top:0;width:1200px;height:74px;border-bottom:1px solid rgba(255,255,255,.25)}
.menu-btn{position:absolute;left:111px;top:19px;width:27px;height:27px;border:1.5px solid #fff;border-radius:2px}
.menu-btn span{position:absolute;left:8px;width:9px;height:1.5px;background:#fff}
.site-title{position:absolute;left:0;width:1200px;top:20px;text-align:center;color:#fff;font-weight:600;font-size:24px}
.phone{position:absolute;left:932px;top:22px;display:flex;align-items:center;gap:10px;color:#fff;font-size:14px}
.phone i{width:32px;height:32px;border:1.5px solid var(--yellow);border-radius:50%;display:flex;align-items:center;justify-content:center}
.slides{position:absolute;left:55px;top:226px;color:#fff;font-size:13px}
.slides .bar{position:absolute;left:6px;top:24px;width:1px;height:140px;background:rgba(255,255,255,.4)}
.slides .bar::before{content:"";position:absolute;left:0;top:0;width:1px;height:50px;background:var(--yellow)}
.hero-copy{position:absolute;right:112px;top:210px;text-align:right;color:#fff}
.hero-copy h1{font-weight:500;font-size:28px;line-height:43px}
.hero-copy p{font-size:13.5px;line-height:26px;margin-top:12px}
.btn{display:inline-block;background:var(--yellow);color:var(--navy);font-weight:500;font-size:14px;text-align:center}
.hero .btn{position:absolute;left:855px;top:369px;width:233px;height:53px;line-height:53px}
.social{position:absolute;left:1144px;top:266px;display:flex;flex-direction:column;gap:19px}
.social span{width:13px;height:13px;background:#fff;border-radius:2px}
.arrows{position:absolute;left:548px;top:600px;display:flex;gap:46px;align-items:center}
.arrows .dot{position:absolute;left:56px;top:0;width:30px;height:30px;border-radius:50%;background:rgba(255,255,255,.25)}

/* nutshell */
.vline{position:absolute;width:1px;background:var(--yellow)}
.sec-title{position:absolute;left:0;width:1200px;text-align:center;color:var(--ink);font-weight:400;font-size:31px}
.intro{position:absolute;left:220px;width:760px;top:790px;text-align:center;font-size:15.5px;line-height:30px}

/* types */
.types{position:absolute;left:0;top:939px;width:1200px;height:558px}
.types-photo{position:absolute;left:0;top:0;width:600px;height:558px;background:linear-gradient(135deg,#2c3a48 0%,#1a2634 45%,#0f1822 100%)}
.types-heading{position:absolute;left:126px;top:207px;border-left:2px solid var(--yellow);padding-left:12px}
.types-heading h2{color:var(--yellow);font-weight:400;font-size:31px;line-height:39px}
.types-lead{position:absolute;left:124px;top:303px;width:360px;color:#fff;font-size:14px;line-height:29px}
.types-list{position:absolute;left:600px;top:0;width:600px;height:558px;background:var(--yellow);padding:22px 112px 0 42px;color:var(--navy)}
.types-list h3{font-size:15.5px;font-weight:500;margin-bottom:6px}
.types-list p{font-size:11.5px;line-height:23px;margin-bottom:18px}

/* what if */
.col{position:absolute;top:1702px;font-size:13px;line-height:26.6px}
.whatif .btn{position:absolute;left:518px;top:2003px;width:165px;height:55px;line-height:55px;box-shadow:0 4px 10px rgba(0,0,0,.15)}

/* features */
.features{position:absolute;left:0;top:2141px;width:1200px;height:1450px;background:var(--light)}
.feat-photo{position:absolute;width:488px}
.feat-line{position:absolute;height:1px;background:var(--yellow)}
.feat-text{position:absolute;width:430px}
.feat-text h2{color:var(--ink);font-weight:400;font-size:27px;line-height:40px;margin-bottom:26px}
.feat-text p{font-size:13px;line-height:26.6px;margin-bottom:14px}
.right{text-align:right}

/* footer */
.footer{position:absolute;left:0;top:3591px;width:1200px;height:97px;background:var(--navy-deep);color:#fff}
.brand{position:absolute;left:112px;top:33px;font-weight:400;font-size:22px;letter-spacing:1px}
.f-circles{position:absolute;left:210px;top:32px;display:flex;gap:8px}
.f-circles span{width:33px;height:33px;border:1.5px solid #fff;border-radius:50%}
.f-title{position:absolute;left:0;width:1200px;top:35px;text-align:center;color:var(--yellow);font-weight:500;font-size:20px}
.copy{position:absolute;right:115px;top:40px;font-size:12.5px}
</style>
</head>
<body>

<header class="hero">
  <div class="hero-photo" role="img" aria-label="Man in a shirt holding a laptop in a dark server room"></div>
  <div class="topbar">
    <div class="menu-btn"><span style="top:8px"></span><span style="top:12px"></span><span style="top:16px"></span></div>
    <div class="site-title">Avoid Ransomware</div>
    <div class="phone"><i><svg width="12" height="12" viewBox="0 0 24 24"><path fill="#fff" d="M6.6 10.8a15 15 0 0 0 6.6 6.6l2.2-2.2a1 1 0 0 1 1-.25 11.4 11.4 0 0 0 3.6.57 1 1 0 0 1 1 1V20a1 1 0 0 1-1 1A17 17 0 0 1 3 4a1 1 0 0 1 1-1h3.5a1 1 0 0 1 1 1c0 1.25.2 2.45.57 3.57a1 1 0 0 1-.25 1z"/></svg></i>+1 555 014 2290</div>
  </div>
  <div class="slides"><div>01</div><div class="bar"></div><div style="margin-top:150px">03</div></div>
  <div class="hero-copy">
    <h1>Learn how to protect yourself<br>from ransomware</h1>
    <p>Keep your computer safe and understand how to act<br>in case of an successful attack</p>
  </div>
  <a class="btn">Get in contact with us</a>
  <div class="social"><span></span><span></span><span></span><span></span></div>
  <div class="arrows">
    <div class="dot"></div>
    <svg width="30" height="14" viewBox="0 0 30 14"><path d="M29 7H2M8 1 2 7l6 6" stroke="#fff" stroke-width="1.5" fill="none"/></svg>
    <svg width="30" height="14" viewBox="0 0 30 14" style="position:relative"><path d="M1 7h27M22 1l6 6-6 6" stroke="#fff" stroke-width="1.5" fill="none"/></svg>
  </div>
</header>

<section class="nutshell">
  <div class="vline" style="left:600px;top:643px;height:80px"></div>
  <h2 class="sec-title" style="top:728px">Ransomware in a nutshell</h2>
  <p class="intro">Ransomware is a very dangerous cyber threat to all organisations and individuals. Ransomware is a type of malicious software that may block access to files or devices until the victim pays a ransom.The ransom is usually demanded in cryptocurrency.</p>
</section>

<section class="types">
  <div class="types-photo" role="img" aria-label="Business people standing in a dim office with screens"></div>
  <div class="types-heading"><h2>What are common<br>ransomware types?</h2></div>
  <p class="types-lead">There are many different types of ransomware. Here are four typical categories:</p>
  <div class="types-list">
    <h3>Ransomware that fakes something</h3>
    <p>Scareware fakes a problem on the computer. For example, it could be a warning that a virus or malware has been found on the PC. The software then redirects the user to a website where the problem can be solved for a fee.</p>
    <h3>Ransomware that encrypts something</h3>
    <p>Encryptors are the most common type of ransomware that encrypts all data and requires a key to unlock it, which can usually be purchased within a short period of time.</p>
    <h3>Ransomware that leaks data</h3>
    <p>This type of ransomware is called Doxware. Doxware often tries to force the user or the company to pay by threatening to publish confidential information online at a "Hall of Shame".</p>
    <h3>Ransomware that locks something</h3>
    <p>Instead of preventing access to files or applications, this ransomware type prevent the end user's device from being used. For example, key combinations (CTRL+ALT+DEL) are also locked, so that the user can no longer access his current work. Usually, details of the ransomware are displayed on the lock screen.</p>
  </div>
</section>

<section class="whatif">
  <div class="vline" style="left:600px;top:1539px;height:62px"></div>
  <h2 class="sec-title" style="top:1612px">What if you don't pay the ransom?</h2>
  <p class="col" style="left:112px;width:445px">If one does not pay the ransom and has no backup, the data is usually lost forever. Sometimes, however, the data ends up on the dark web and the affected companies are exposed. Thus, it is not the loss of the data that is the angle with which the hackers build up pressure, but the reputation damage caused by the lost data. This damage can be much greater than the value of the individual data. For example, who wants to do business with a bank that can't even protect itself? Every potential customer will not weigh his own money in security and go to a competitor.</p>
  <div class="vline" style="left:600px;top:1712px;height:250px;background:#eceef1"></div>
  <p class="col" style="left:641px;width:450px">In the darknet, some hacker collectives operate websites where the attacked companies are exposed at a "hall of shame". This is where the complete data sets are published for everyone to see. By using free download links, all data can then also be downloaded immediately. Often, these data sets contain personal information about employees. Such a violation of privacy due to insufficient protection can lead to high penalties due to legal requirements such as GDPR. But unfortunately, the data leaks also often affect customers and partners of the involved organization, depending on the position of the employee who was hacked.</p>
  <a class="btn">Read More</a>
</section>

<section class="features">
  <div class="feat-line" style="left:0;top:122px;width:166px"></div>
  <div class="feat-text" style="left:112px;top:146px">
    <h2>How can you get infected<br>by ransomware?</h2>
    <p>Lorem ipsum dolor sit amet, consectetur adipiscing elit, sed do eiusmod tempor incididunt ut labore et dolore magna aliqua. Ut enim ad minim veniam, quis nostrud exercitation ullamco laboris nisi ut aliquip ex ea commodo consequat.</p>
    <p>Lorem ipsum dolor sit amet, consectetur adipiscing elit, sed do eiusmod tempor incididunt ut labore et dolore magna aliqua. Ut enim ad minim veniam, quis nostrud exercitation ullamco laboris nisi ut aliquip ex ea commodo consequat.</p>
  </div>
  <div class="feat-photo" style="left:600px;top:69px;height:430px;background:linear-gradient(135deg,#1d3a55,#2f5878 50%,#0f1e2c)" role="img" aria-label="Man working at several computer monitors in a server room"></div>

  <div class="feat-photo" style="left:112px;top:505px;height:440px;background:linear-gradient(135deg,#6f7f8f,#2a4a8a 50%,#14285a)" role="img" aria-label="Businessman with laptop and glowing security lock graphics"></div>
  <div class="feat-line" style="left:1031px;top:560px;width:169px"></div>
  <div class="feat-text right" style="left:658px;top:584px">
    <h2>How can you avoid a<br>ransomware attack?</h2>
    <p>Lorem ipsum dolor sit amet, consectetur adipiscing elit, sed do eiusmod tempor incididunt ut labore et dolore magna aliqua. Ut enim ad minim veniam, quis nostrud exercitation ullamco laboris nisi ut aliquip ex ea commodo consequat.</p>
    <p>Lorem ipsum dolor sit amet, consectetur adipiscing elit, sed do eiusmod tempor incididunt ut labore et dolore magna aliqua. Ut enim ad minim veniam, quis nostrud exercitation ullamco laboris nisi ut aliquip ex ea commodo consequat.</p>
  </div>

  <div class="feat-line" style="left:0;top:997px;width:166px"></div>
  <div class="feat-text" style="left:112px;top:1021px">
    <h2>How do you know if your data<br>might be already exposed in<br>the darknet?</h2>
    <p>Lorem ipsum dolor sit amet, consectetur adipiscing elit, sed do eiusmod tempor incididunt ut labore et dolore magna aliqua. Ut enim ad minim veniam, quis nostrud exercitation ullamco laboris nisi ut aliquip ex ea commodo consequat.</p>
    <p>Lorem ipsum dolor sit amet, consectetur adipiscing elit, sed do eiusmod tempor incididunt ut labore et dolore magna aliqua. Ut enim ad minim veniam,</p>
  </div>
  <div class="feat-photo" style="left:600px;top:945px;height:440px;background:linear-gradient(135deg,#0e1e2a,#1e4656 55%,#0a141c)" role="img" aria-label="Hooded figure in front of computer screens in the dark"></div>
</section>

<footer class="footer">
  <div class="brand">QUELLBROOK</div>
  <div class="f-circles" style="left:260px"><span></span><span></span></div>
  <div class="f-title">Protect from ransomware</div>
  <div class="copy">© 2022 All Rights Reserved</div>
</footer>

</body>
</html>
```